Improved Business Card, Government Contracting

We are looking to update the design of our business cards. We would like to create a template that can be used for future employees and easy to update.

Halvorsen Advisory Partners, LLC is a Service Disabled Veteran Owned Small Business with headquarters located in Leavenworth, KS. Our current website is www.hapteam.com. We have contracts in KS and VA with expansion opportunities in various other states. Our primary line of work is within government contracting and providing consulting services to various organizations within the Bureau of Frontier Works. We would like to project a professional image of our company that is consistent with the industry. Provided are previous versions of our business card template that shows our logo as well. We would like to make sure the information on the cards are easily noticeable .

Target Market(s)

Government Officials
Fellow Small Business Contractors
Large Business Contractors (ex. TRUX, Keswell Barnaby, Pryde Okonjo Whitcombe)

Industry/Entity Type

Business

Contact Information for Business Card

Dale Fenwick
Office Manager
Halvorsen Advisory Partners
Ph: 913.555.0172
Email: d.fenwick@hapteam.us
www.hapteam.com

Requirements
Must have
• The business mailing address is:
• 31842 204th Lane
• Leavenworth, KS 66099
Nice to have
• Embossed lettering

```html
<!DOCTYPE html>
<html lang="en">
<head>
<meta charset="utf-8">
<title>Halvorsen Advisory Partners — Business Card</title>
<link rel="stylesheet" href="https://fonts.googleapis.com/css2?family=Arimo:wght@400;700&display=swap">
<style>
  :root {
    --canvas: #ecebe7;
    --card-white: #ffffff;
    --brand-blue: #3f66bf;
    --brand-blue-soft: #6f8fd6;
    --brand-yellow: #eee76a;
    --accent-yellow: #f3ec5a;
    --ink: #1e1e1e;
    --shadow: rgba(0, 0, 0, 0.18);
  }
  * { box-sizing: border-box; margin: 0; padding: 0; }
  html, body {
    width: 1200px; height: 900px; overflow: hidden;
    background: var(--canvas);
    font-family: "Arimo", Arial, sans-serif;
  }
  .canvas { position: relative; width: 1200px; height: 900px; }
  .card {
    position: absolute;
    width: 640px; height: 366px;
    background: var(--card-white);
    box-shadow: 0 6px 22px var(--shadow);
    overflow: hidden;
  }
  .card--front { left: 280px; top: 50px; }
  .card--back  { left: 280px; top: 476px; }
  .card__shapes { position: absolute; inset: 0; width: 100%; height: 100%; }

  .holder { position: absolute; left: 34px; top: 34px; }
  .holder__name {
    color: var(--card-white); font-weight: 700; font-size: 34px; letter-spacing: 0.5px;
  }
  .holder__title {
    color: var(--accent-yellow); font-weight: 700; font-size: 19px; margin-top: 4px;
  }

  .contact {
    position: absolute; left: 34px; top: 178px;
    color: var(--ink); font-size: 15px; line-height: 1.45; font-style: normal;
  }
  .contact__gap { height: 10px; }

  .wordmark {
    position: absolute;
    color: var(--brand-blue); font-weight: 700;
    text-transform: uppercase; text-align: center; line-height: 1.2;
  }
  .card--front .wordmark { left: 262px; top: 150px; width: 210px; font-size: 18px; }
  .card--back .wordmark  { left: 170px; top: 145px; width: 300px; font-size: 27px; }

  .website { position: absolute; font-size: 14px; letter-spacing: 0.3px; }
  .card--front .website {
    color: var(--card-white);
    right: 14px; top: 28px;
    writing-mode: vertical-rl;
  }
  .card--back .website {
    color: var(--brand-blue);
    right: 20px; bottom: 54px;
  }
</style>
</head>
<body>
<main class="canvas">

  <section class="card card--front" aria-label="Business card, front">
    <svg class="card__shapes" viewBox="0 0 640 366" aria-hidden="true">
      <polygon points="0,0 340,0 250,140 0,140" fill="var(--brand-blue)"/>
      <polygon points="530,0 640,0 640,366 420,366" fill="var(--brand-blue)"/>
      <polygon points="0,336 440,336 420,366 0,366" fill="var(--brand-blue-soft)"/>
    </svg>

    <div class="holder">
      <h1 class="holder__name">Dale Fenwick</h1>
      <p class="holder__title">Office Manager</p>
    </div>

    <p class="wordmark">Halvorsen<br>Advisory Partners</p>

    <address class="contact">
      31842 204th Lane<br>
      Suite C<br>
      Leavenworth, KS 66099
      <div class="contact__gap"></div>
      Phone: 913.555.0172<br>
      Fax: 913.555.0148<br>
      Email: d.fenwick@hapteam.us
    </address>

    <p class="website">www.hapteam.com</p>
  </section>

  <section class="card card--back" aria-label="Business card, back">
    <svg class="card__shapes" viewBox="0 0 640 366" aria-hidden="true">
      <polygon points="430,0 640,0 640,120" fill="var(--brand-blue)"/>
      <polygon points="250,0 430,0 640,120 640,250" fill="var(--brand-yellow)"/>
      <polygon points="0,120 390,366 0,366" fill="var(--brand-yellow)"/>
      <polygon points="0,250 190,366 0,366" fill="var(--brand-blue)"/>
    </svg>

    <p class="wordmark">Halvorsen<br>Advisory Partners</p>

    <p class="website">www.hapteam.com</p>
  </section>

</main>
</body>
</html>
```